We need a new design for our landing page. The baseline for the design should be our current landing page, that can be found on this page:
https://www.vorlani.com/convert/
We are quite open for making visual changes on this page. This means you have to respect the flow and the text, but all other components are up for a challenge if you feel that there are better ways of showing the page components.
The requirements are:
The page should be designed for computer view only.
The communication and the flow of the components on the current page must be unchanged.
The target group for the page is small and medium-sized business owners who have a website that generates some business to them (sales, contact collections etc.).They do not understand web analytics and are looking for an easy way to do so for them. Our solution helps them achieve this.
The challenge that we have with the current page is that the users do not discover how great our product is and how it actually can help them.
We provide an automated web analytics solution that tells them how to best improve their website.
This can be best illustrated with the attached page from our product. This tells you where to focus to improve your site's conversions.
We need this illustration to be a significant part of the top of the landing page, together with the wordings that are there already. Please note that this is not from a web-based dashboard, it is a page in a PDF report. This (current) text must be a part if the top of the page:"Vorlani is the automated web analytics PDF report, that lets you boost conversions by:Understanding why your users convertDriving converting traffic to your siteOptimising your navigation and engagementImprove your user flows."
It is ok if you have suggestions on how to do the last part of the landing page as well, but we are ok with that part of the flow.If you look at the other pages of our site, you will see that we try to make it clean and elegant, and this should be an aim for the landing page too.
We have a corporate colour pallet that I would like you to follow. The hex values are:
00C2E8
832926
027C74
036760
8FB1BC
The style we are looking for could be something like this:
https://pagebrisk.com/en-au/
Also we have e new project explainer video that you can include in stead of the "Know all your growth opportunities" section, It can be found on this page:
https://files.example-store.net/file/d/7Kq4TmZpW2xRb9LcNvH3yDfJ8sQa5EgU1/view
Finally. If you tink that there is too much information on the page, then it is ok for you to remove some components such as:
The world map
The benefits at a glance section
Web Analytics Out of the Box
Target Market(s)
Business owners from Small and medium sized business
Number of Pages Required
1 page

```html
<!DOCTYPE html>
<html lang="en">
<head>
<meta charset="utf-8">
<title>Vorlani – Automated Web Analytics PDF Report</title>
<link href="https://fonts.googleapis.com/css2?family=Saira+Condensed:wght@500;600&family=Poppins:wght@400;500&family=Roboto:wght@400;500;700&family=Roboto+Condensed:wght@400;500&display=swap" rel="stylesheet">
<style>
  :root{
    --cyan:#00C2E8;
    --maroon:#832926;
    --teal:#027C74;
    --teal-dark:#036760;
    --mist:#8FB1BC;
    --mist-light:#c9dbe1;
    --maroon-dark:#5c1a18;
    --ink:#1c1c1c;
    --grey:#555;
    --black:#0a0a0a;
    --white:#fff;
  }
  *{box-sizing:border-box;margin:0;padding:0}
  html,body{width:1200px;height:4826px;overflow:hidden}
  body{position:relative;background:var(--white);font-family:"Roboto",sans-serif;color:var(--ink)}
  .abs{position:absolute}

  /* header */
  .site-header{position:absolute;top:0;left:0;width:1200px;height:110px}
  .brand{position:absolute;left:158px;top:38px;display:flex;align-items:center;gap:10px;font-weight:500;font-size:24px;letter-spacing:3px;color:#2f3b45}
  .brand-dot{width:32px;height:32px;border-radius:50%;border:3px solid var(--teal)}
  .main-nav{position:absolute;right:155px;top:48px;display:flex;gap:28px;align-items:center;font-size:14px;color:#333}
  .nav-cta{background:var(--teal);color:var(--white);border-radius:14px;padding:5px 16px}

  /* hero */
  .hero-title{position:absolute;top:138px;left:0;width:1200px;text-align:center;font-family:"Saira Condensed",sans-serif;font-weight:600;font-size:42px;line-height:52px;color:var(--teal)}
  .benefits{position:absolute;top:285px;left:232px;width:760px;display:grid;grid-template-columns:415px 345px;row-gap:14px;font-size:16px;color:#222}
  .benefits li{list-style:none;display:flex;align-items:center;gap:9px}
  .tick{width:18px;height:18px;flex:none}
  .hero-band{position:absolute;top:420px;left:0;width:1200px;height:450px}
  .hero-side{position:absolute;top:480px;width:230px;height:200px;border-radius:8px;background:linear-gradient(180deg,rgba(255,255,255,.35),rgba(3,103,96,.18))}
  .hero-report{position:absolute;top:430px;left:390px;width:420px;height:306px;box-shadow:0 14px 30px rgba(3,60,56,.35)}

  /* comparison */
  .compare-card{position:absolute;top:980px;width:403px;height:212px;background:var(--white);border-radius:30px;box-shadow:0 4px 18px rgba(0,0,0,.14);text-align:center;padding:78px 44px 0}
  .compare-card h3{font-family:"Poppins",sans-serif;font-weight:500;font-size:26px;color:#111;margin-bottom:10px}
  .compare-card p{font-size:13px;line-height:19px;color:#444}
  .compare-icon{position:absolute;top:-52px;left:50%;margin-left:-52px;width:104px;height:104px;border-radius:50%;background:var(--teal);border:6px solid #e4f0ef;display:flex;align-items:center;justify-content:center}

  /* report band */
  .report-band{position:absolute;top:1265px;left:0;width:1200px;height:520px;background:linear-gradient(135deg,var(--teal-dark),var(--teal) 65%,#04968c)}
  .report-frame{position:absolute;left:135px;top:108px;width:300px;height:260px;border:2px solid var(--white)}
  .report-page{position:absolute;left:155px;top:125px;width:432px;height:315px}
  .report-copy{position:absolute;left:622px;top:170px;width:440px;color:var(--white)}
  .report-copy h2{font-weight:400;font-size:25px;line-height:31px;margin-bottom:16px}
  .report-copy p{font-size:18px;line-height:27px;margin-bottom:22px}
  .btn-outline{display:inline-block;border:1.5px solid var(--white);border-radius:18px;padding:8px 24px;font-size:13px;letter-spacing:.5px;color:var(--white)}

  /* services */
  .section-title{position:absolute;left:0;width:1200px;text-align:center;font-family:"Poppins",sans-serif;font-weight:400;font-size:40px;color:#111}
  .service{position:absolute;width:415px}
  .service h3{font-family:"Roboto Condensed",sans-serif;font-weight:400;font-size:28px;color:#111;margin-bottom:20px}
  .service p{font-size:14px;line-height:21px;color:var(--grey);margin-bottom:10px;text-align:justify}
  .service-ring{position:absolute;width:300px;height:300px;border-radius:50%;border:2px solid var(--maroon);background:var(--white)}
  .service-art{position:absolute;left:14px;top:14px;width:268px;height:268px;border-radius:50%}
  .art-teal{background:radial-gradient(circle,#12948a,var(--teal-dark))}
  .art-cyan{background:radial-gradient(circle,#37d2f0,#0098b8)}
  .art-mist{background:radial-gradient(circle,#f3f8f9,var(--mist-light))}

  /* about */
  .about-band{position:absolute;top:3259px;left:0;width:1200px;height:537px;background:linear-gradient(120deg,#a8403a,var(--maroon) 55%,var(--maroon-dark))}
  .about-copy{position:absolute;left:160px;top:140px;width:455px;color:var(--white)}
  .about-copy h2{font-family:"Poppins",sans-serif;font-weight:400;font-size:40px;margin-bottom:10px}
  .about-copy p{font-size:14px;line-height:21px}
  .about-copy .btn-outline{margin-top:30px;padding:6px 18px;font-size:13px}
  .video-frame{position:absolute;left:760px;top:70px;width:308px;height:165px;border:2px solid var(--white)}
  .video-box{position:absolute;left:634px;top:108px;width:412px;height:300px}
  .video-art{position:absolute;inset:0;background:linear-gradient(160deg,#1f3d40,#13282a)}
  .play{position:absolute;left:50%;top:50%;width:58px;height:58px;margin:-29px 0 0 -29px;border-radius:50%;background:rgba(255,255,255,.92)}

  /* integrations */
  .platforms{position:absolute;top:4010px;left:210px;width:780px;display:grid;grid-template-columns:repeat(4,1fr);row-gap:48px}
  .platform{display:flex;align-items:center;justify-content:center;gap:8px;font-weight:700;font-size:28px;color:#3a3a3a}
  .platform-mark{width:22px;height:22px;border-radius:50%;background:#3a3a3a;flex:none}
  .btn-solid{position:absolute;top:4205px;left:490px;width:220px;height:48px;border-radius:24px;background:var(--teal);color:var(--white);font-size:16px;letter-spacing:.5px;display:flex;align-items:center;justify-content:center}

  /* footer */
  .site-footer{position:absolute;top:4290px;left:0;width:1200px;height:536px}
  .footer-cols{position:absolute;top:4460px;left:158px;width:890px;height:200px;color:var(--white)}
  .footer-col{position:absolute;top:0}
  .footer-col h4{font-weight:500;font-size:15px;letter-spacing:.5px;margin-bottom:28px}
  .footer-col li{list-style:none;font-size:13px;line-height:29px}
  .contact-line{display:flex;gap:10px;margin-bottom:18px;font-size:12px;line-height:16px}
  .contact-line b{font-weight:500;display:block}
  .field{width:266px;height:30px;background:var(--white);margin-bottom:16px;color:#888;font-size:12px;padding:7px 10px}
  .send{width:110px;height:30px;background:var(--teal);color:var(--white);font-size:14px;display:flex;align-items:center;justify-content:center}
  .footer-rule{position:absolute;top:4730px;left:158px;width:888px;height:1px;background:#333}
  .copyright{position:absolute;top:4747px;left:0;width:1200px;text-align:center;font-size:12px;color:var(--white)}
  .lang{position:absolute;top:4747px;left:1128px;font-size:12px;color:var(--white)}
</style>
</head>
<body>

<svg width="0" height="0" style="position:absolute">
  <defs>
    <symbol id="report-sheet" viewBox="0 0 432 315">
      <rect width="432" height="315" fill="#fff"/>
      <g font-family="Roboto, sans-serif" text-anchor="middle">
        <text x="216" y="22" font-size="8" fill="#555" letter-spacing="1">RESULTS</text>
        <line x1="186" y1="28" x2="246" y2="28" stroke="#8FB1BC"/>
        <g font-size="7" fill="#333" font-weight="500">
          <text x="76" y="44">USER EXPERIENCE</text>
          <text x="216" y="44">CONVERSION CONTENT</text>
          <text x="356" y="44">USER JOURNEY</text>
        </g>
        <line x1="40" y1="50" x2="392" y2="50" stroke="#dde6e9"/>
        <circle cx="76" cy="96" r="38" fill="#8FB1BC"/>
        <circle cx="216" cy="96" r="38" fill="#8FB1BC"/>
        <circle cx="356" cy="96" r="38" fill="#8FB1BC"/>
        <g font-size="10" fill="#fff" font-weight="500">
          <text x="76" y="92">Score</text><text x="76" y="106">72</text>
          <text x="216" y="92">Score</text><text x="216" y="106">64</text>
          <text x="356" y="92">Score</text><text x="356" y="106">81</text>
        </g>
        <text x="216" y="168" font-size="8" fill="#555" letter-spacing="1">ACTIONS</text>
        <line x1="186" y1="174" x2="246" y2="174" stroke="#8FB1BC"/>
        <g font-size="7" fill="#333" font-weight="500">
          <text x="76" y="192">MARKETING</text>
          <text x="216" y="192">MERCHANDISE</text>
          <text x="356" y="192">SOCIAL MEDIA</text>
        </g>
        <line x1="40" y1="198" x2="392" y2="198" stroke="#dde6e9"/>
        <circle cx="76" cy="246" r="38" fill="#8FB1BC"/>
        <circle cx="216" cy="246" r="38" fill="#8FB1BC"/>
        <circle cx="356" cy="246" r="38" fill="#8FB1BC"/>
        <g font-size="10" fill="#fff" font-weight="500">
          <text x="76" y="242">Score</text><text x="76" y="256">58</text>
          <text x="216" y="242">Score</text><text x="216" y="256">69</text>
          <text x="356" y="242">Score</text><text x="356" y="256">47</text>
        </g>
      </g>
    </symbol>
  </defs>
</svg>

<header class="site-header">
  <div class="brand"><span class="brand-dot"></span>VORLANI</div>
  <nav class="main-nav">
    <span>Product</span><span>Prices</span><span>Agency</span><span>Request demo</span><span>Try for free</span><span>Support</span><span class="nav-cta">Sign up</span>
  </nav>
</header>

<section class="hero">
  <h1 class="hero-title">Vorlani is the easy to read automated web analytics<br>PDF report, that lets you boost conversions by:</h1>
  <ul class="benefits">
    <li><svg class="tick" viewBox="0 0 18 18"><circle cx="9" cy="9" r="9" fill="#027C74"/><path d="M5 9.3l2.6 2.6L13 6.5" fill="none" stroke="#fff" stroke-width="2"/></svg>Understanding why your users convert</li>
    <li><svg class="tick" viewBox="0 0 18 18"><circle cx="9" cy="9" r="9" fill="#027C74"/><path d="M5 9.3l2.6 2.6L13 6.5" fill="none" stroke="#fff" stroke-width="2"/></svg>Driving converting traffic to your site</li>
    <li><svg class="tick" viewBox="0 0 18 18"><circle cx="9" cy="9" r="9" fill="#027C74"/><path d="M5 9.3l2.6 2.6L13 6.5" fill="none" stroke="#fff" stroke-width="2"/></svg>Optimizing your navigation and engagement</li>
    <li><svg class="tick" viewBox="0 0 18 18"><circle cx="9" cy="9" r="9" fill="#027C74"/><path d="M5 9.3l2.6 2.6L13 6.5" fill="none" stroke="#fff" stroke-width="2"/></svg>Improve your user flows</li>
  </ul>
  <svg class="hero-band" viewBox="0 0 1200 450" preserveAspectRatio="none">
    <path d="M0 15 Q600 130 1200 15 L1200 335 Q600 480 0 335 Z" fill="#8FB1BC"/>
  </svg>
  <div class="hero-side" style="left:130px" role="img" aria-label="Isometric illustration of a website owner at a laptop platform"></div>
  <div class="hero-side" style="left:840px" role="img" aria-label="Isometric illustration of the report arriving on a laptop"></div>
  <svg class="abs" style="left:360px;top:570px" width="480" height="40" viewBox="0 0 480 40">
    <path d="M0 20H24M456 20H480" stroke="#fff" stroke-width="2" stroke-dasharray="4 4"/>
  </svg>
  <svg class="hero-report" viewBox="0 0 432 315" role="img" aria-label="Page from the Vorlani PDF report showing scores by improvement area"><use href="#report-sheet"/></svg>
</section>

<section class="compare">
  <div class="compare-card" style="left:160px">
    <div class="compare-icon"><svg width="46" height="40" viewBox="0 0 46 40"><rect x="2" y="2" width="42" height="28" rx="2" fill="none" stroke="#fff" stroke-width="3"/><path d="M17 38h12M23 30v8" stroke="#fff" stroke-width="3"/></svg></div>
    <h3>The old way</h3>
    <p>A skilled web analytics expert analysed your website, so you could drive your business in a true data-driven way.</p>
  </div>
  <div class="compare-card" style="left:637px">
    <div class="compare-icon"><svg width="42" height="40" viewBox="0 0 42 40"><rect x="2" y="2" width="38" height="36" rx="2" fill="none" stroke="#fff" stroke-width="3"/><path d="M11 30V20M17 30V12M23 30V16M29 30V9" stroke="#fff" stroke-width="3"/></svg></div>
    <h3>The new way</h3>
    <p>Vorlani is based on AI and mimics the tasks that a skilled analytics expert would have performed if he were to analyze your website.</p>
  </div>
</section>

<section class="report-band">
  <div class="report-frame"></div>
  <svg class="report-page" viewBox="0 0 432 315" role="img" aria-label="Sample page from the Vorlani PDF report"><use href="#report-sheet"/></svg>
  <div class="report-copy">
    <h2>Vorlani is the smart web analytics report that identifies your best improvement options</h2>
    <p>Delivered to you in a beautifully designed and easy to understand PDF report</p>
    <span class="btn-outline">DOWNLOAD SAMPLE REPORT</span>
  </div>
</section>

<h2 class="section-title" style="top:1925px">Our Services</h2>

<svg class="abs" style="left:0;top:2150px" width="1200" height="900" viewBox="0 0 1200 900">
  <path d="M735 160 L457 346" stroke="#832926" stroke-width="1.5"/>
  <circle cx="735" cy="160" r="7" fill="#832926"/>
  <circle cx="457" cy="346" r="7" fill="#832926"/>
  <path d="M457 555 L734 787" stroke="#832926" stroke-width="1.5"/>
  <circle cx="457" cy="555" r="7" fill="#832926"/>
  <circle cx="734" cy="787" r="7" fill="#832926"/>
</svg>

<div class="service" style="left:232px;top:2118px">
  <h3>Don't Learn Web Analytics</h3>
  <p>You don't have to learn the complexity of web analytics.</p>
  <p>If you've ever tried to get an accurate picture of how visitors REALLY behave, you'll know that website analytics are incredibly complicated.</p>
</div>
<div class="service-ring" style="left:712px;top:2070px"><div class="service-art art-teal" role="img" aria-label="Illustration of people working around a laptop with analytics charts"></div></div>

<div class="service-ring" style="left:195px;top:2440px"><div class="service-art art-cyan" role="img" aria-label="Illustration of a computer screen with a target and website improvement icons"></div></div>
<div class="service" style="left:547px;top:2520px">
  <h3>Don't Ever Guess Again</h3>
  <p>You don't have to guess how to improve your site.</p>
  <p>Vorlani software tells you exactly which improvement options on your site that has the best potential.</p>
</div>

<div class="service" style="left:232px;top:2915px">
  <h3>Don't Waste Your Time</h3>
  <p>You don't have to spend time gathering data.</p>
  <p>Vorlani provides you with Growth Reports on your site's core areas, giving you automatic web analytics reports. So you don't have to spend time using yet another new tool.</p>
</div>
<div class="service-ring" style="left:712px;top:2826px"><div class="service-art art-mist" role="img" aria-label="Illustration of a large clock with people and a paper plane, representing saved time"></div></div>

<section class="about-band">
  <div class="about-copy">
    <h2>About us</h2>
    <p>Improving your website is an ongoing improvement task which you should search for areas that are either easy to implement or has a high potential value output.<br>The report will guide you through the improvement process and let you know what your options are so that you can make informed choices on what will grow your business the most.</p>
    <span class="btn-outline">Read More</span>
  </div>
  <div class="video-frame"></div>
  <div class="video-box">
    <div class="video-art" role="img" aria-label="Vorlani project explainer video still"></div>
    <div class="play"><svg width="58" height="58" viewBox="0 0 58 58"><path d="M23 18l16 11-16 11z" fill="#036760"/></svg></div>
  </div>
</section>

<h2 class="section-title" style="top:3905px;font-size:38px">Getting started is easy</h2>
<div class="platforms">
  <div class="platform"><span class="platform-mark"></span>Pressly</div>
  <div class="platform" style="font-size:18px;font-weight:400">Tagwise Manager</div>
  <div class="platform">Sitebox</div>
  <div class="platform"><span class="platform-mark"></span>Corewell</div>
  <div class="platform"><span class="platform-mark"></span>Shopnest</div>
  <div class="platform" style="font-weight:400">Cartora</div>
  <div class="platform"><span class="platform-mark"></span>Jumbly</div>
  <div class="platform">Droply</div>
</div>
<div class="btn-solid">TRY FOR FREE</div>

<footer>
  <svg class="site-footer" viewBox="0 0 1200 536" preserveAspectRatio="none">
    <path d="M0 50 L1200 0 L1200 536 L0 536 Z" fill="#00C2E8"/>
    <path d="M0 80 L1200 30 L1200 536 L0 536 Z" fill="#0a0a0a"/>
  </svg>
  <div class="footer-cols">
    <div class="footer-col" style="left:0">
      <h4>CONTACT US</h4>
      <div class="contact-line"><svg width="16" height="12" viewBox="0 0 16 12"><rect x="1" y="1" width="14" height="10" fill="none" stroke="#fff"/><path d="M1 1l7 6 7-6" fill="none" stroke="#fff"/></svg><span><b>EMAIL ADDRESS</b>hello@vorlani.com</span></div>
      <div class="contact-line"><svg width="16" height="16" viewBox="0 0 16 16"><path d="M4 1l3 3-2 2q2 4 5 5l2-2 3 3-2 3Q5 14 1 3z" fill="none" stroke="#fff"/></svg><span><b>PHONE NUMBER</b>0600 123 456</span></div>
    </div>
    <div class="footer-col" style="left:254px">
      <h4>LINKS</h4>
      <ul><li>Home</li><li>About Us</li><li>Content analytics</li><li>Press</li></ul>
    </div>
    <div class="footer-col" style="left:434px">
      <h4>RESOURCES</h4>
      <ul><li>Cookie Information</li><li>FAQ</li><li>Legal</li><li>Contact Us</li></ul>
    </div>
    <div class="footer-col" style="left:621px">
      <h4>GET IN TOUCH</h4>
      <div class="field">Your Name</div>
      <div class="field">Email address</div>
      <div class="field">Phone</div>
      <div class="send">SEND</div>
    </div>
  </div>
  <div class="footer-rule"></div>
  <div class="copyright">© Copyright 2019 . All Rights Reserved. Terms and Conditions | Privacy Policy</div>
  <div class="lang">EN</div>
</footer>

</body>
</html>
```